Vor Plimm business card

Create a new business card for Vor Plimm. Black colour base front and back (the sides can be blue if that works) You can modify the blue colour to best suit the design. I am after a card that looks technical, modern and strong. one side with the Vor Plimm and the other company details. The attached file has the details needed for the card. Tarnwell is the parent company name and needed but in a smaller size

Target Market(s)

Businesses (suppliers and customers)

Industry/Entity Type

Business

Contact Information for Business Card

Black colour base front and back

Font styles to use
Other font styles liked:
• attached

Requirements
Must have
• Logo's as attached

```html
<!DOCTYPE html>
<html lang="en">
<head>
<meta charset="utf-8">
<title>Vor Plimm business card</title>
<link rel="stylesheet" href="https://fonts.googleapis.com/css2?family=Open+Sans:wght@400;600;700&display=swap">
<style>
  :root {
    --backdrop: #3a3a3a;
    --card: #2b2b2c;
    --silver: #c9ccd0;
    --white: #f4f4f4;
    --blue: #2f6fc4;
    --grey: #6b6b6d;
    --divider: #d8d8d8;
  }
  * { margin: 0; padding: 0; box-sizing: border-box; }
  html, body {
    width: 1200px; height: 900px; overflow: hidden;
    background: var(--backdrop);
    font-family: "Open Sans", Arial, sans-serif;
  }
  .card {
    position: absolute; left: 75px; top: 150px;
    width: 1050px; height: 600px;
    background: var(--card);
    box-shadow: 0 20px 40px rgba(0,0,0,.45);
  }
  .brand {
    position: absolute; left: 110px; top: 120px;
    font-weight: 700; font-size: 64px; letter-spacing: 6px;
    text-transform: uppercase; color: var(--silver);
  }
  .parent {
    position: absolute; left: 110px; top: 330px;
  }
  .parent-name {
    font-weight: 700; font-size: 52px; line-height: 1;
    color: var(--blue);
  }
  .parent-legal {
    margin-top: 10px; font-size: 13px; color: var(--grey);
  }
  .divider {
    position: absolute; left: 545px; top: 150px;
    width: 2px; height: 300px; background: var(--divider);
  }
  .contact {
    position: absolute; left: 600px; top: 150px;
    color: var(--white);
  }
  .person-name { font-weight: 700; font-size: 34px; line-height: 1.1; }
  .person-role { font-size: 21px; margin-top: 2px; }
  .details { list-style: none; margin-top: 28px; font-size: 21px; line-height: 1.3; }
  .details li { display: flex; align-items: flex-start; gap: 10px; }
  .details li + li { margin-top: 2px; }
  .details li.gap { margin-top: 22px; }
  .icon { width: 22px; height: 22px; flex: none; margin-top: 3px; }
</style>
</head>
<body>
  <main class="card">
    <div class="brand">Vor Plimm</div>

    <div class="parent">
      <div class="parent-name">Tarnwell</div>
      <div class="parent-legal">Tarnwell International Pty Ltd</div>
    </div>

    <div class="divider"></div>

    <section class="contact">
      <div class="person-name">Rion Halvek</div>
      <div class="person-role">Managing Director</div>
      <ul class="details">
        <li>
          <svg class="icon" viewBox="0 0 22 22" aria-hidden="true"><circle cx="11" cy="11" r="10" fill="none" stroke="#f4f4f4" stroke-width="1.6"/><path d="M7 8c0 4 3 7 7 7l1-2-2-1-1 1c-1-.5-2-1.5-2.5-2.5l1-1-1-2z" fill="#f4f4f4"/></svg>
          <span>+61 400 555 019</span>
        </li>
        <li>
          <svg class="icon" viewBox="0 0 22 22" aria-hidden="true"><circle cx="11" cy="11" r="10" fill="none" stroke="#f4f4f4" stroke-width="1.6"/><rect x="6" y="7.5" width="10" height="7" fill="#f4f4f4"/><path d="M6 7.5l5 4 5-4" fill="none" stroke="#2b2b2c" stroke-width="1.2"/></svg>
          <span>rion@tarnwellint.com</span>
        </li>
        <li class="gap">
          <svg class="icon" viewBox="0 0 22 22" aria-hidden="true"><circle cx="11" cy="11" r="10" fill="none" stroke="#f4f4f4" stroke-width="1.6"/><path d="M11 17c-3-4-4.5-6-4.5-8a4.5 4.5 0 0 1 9 0c0 2-1.5 4-4.5 8z" fill="#f4f4f4"/><circle cx="11" cy="9" r="1.6" fill="#2b2b2c"/></svg>
          <span>PO Box 118 Eastvale<br>S.A. 5000<br>Australia</span>
        </li>
        <li>
          <svg class="icon" viewBox="0 0 22 22" aria-hidden="true"><circle cx="11" cy="11" r="10" fill="none" stroke="#f4f4f4" stroke-width="1.6"/><circle cx="11" cy="11" r="6" fill="none" stroke="#f4f4f4" stroke-width="1.2"/><ellipse cx="11" cy="11" rx="2.5" ry="6" fill="none" stroke="#f4f4f4" stroke-width="1.2"/><path d="M5 11h12" stroke="#f4f4f4" stroke-width="1.2"/></svg>
          <span>www.tarnwellint.com</span>
        </li>
      </ul>
    </section>
  </main>
</body>
</html>
```